Haskell and Dunmore Ranch Insurance

Would like you all to design a logo for our Business cards and possible letterhead.
This business provides Ranch insurance for folks in Texas, New Mexico, and Oklahoma

Ggood stuff everybody, be sure to include email and Mobil for both of us on all designs

Thanks

Hello All

Wanted to let you all know i am going to extend deadline a few days, and add some more $$ to the budget

Reason: Give everybody a bit ,more time, and I added more money

Appreciate all of yalls hard work, will review and provide feed back hopefully today, been a little whacky with the holidays and all

```html
<!DOCTYPE html>
<html lang="en">
<head>
<meta charset="utf-8">
<title>Haskell and Dunmore – Stationery</title>
<link rel="stylesheet" href="https://fonts.googleapis.com/css2?family=Comfortaa:wght@400;700&family=Quicksand:wght@500;700&display=swap">
<style>
  :root {
    --backdrop: #e9e6e1;
    --sheet: #bacefd;
    --sheet-header: #c6d7fd;
    --stripe: #ffffff;
    --card: #6699ff;
    --ink: #0d1a3a;
    --ink-soft: #1d2a4a;
    --white: #ffffff;
  }
  * { box-sizing: border-box; margin: 0; padding: 0; }
  html, body { width: 1200px; height: 1000px; overflow: hidden; }
  body { background: var(--backdrop); position: relative; font-family: "Quicksand", sans-serif; color: var(--ink); }

  /* Letterhead */
  .letterhead {
    position: absolute; left: 70px; top: 80px; width: 640px; height: 840px;
    background: var(--sheet); box-shadow: 0 4px 14px rgba(0,0,0,0.18);
  }
  .letterhead__header {
    position: absolute; left: 0; top: 0; width: 100%; height: 118px;
    background: var(--sheet-header);
  }
  .letterhead__stripe { position: absolute; left: 0; width: 100%; height: 20px; background: var(--stripe); }
  .letterhead__stripe--top { top: 118px; }
  .letterhead__stripe--bottom { bottom: 110px; }
  .brand-dot { position: absolute; border-radius: 50%; background: var(--white); }
  .letterhead .brand-dot { left: 30px; top: 30px; width: 46px; height: 46px; }
  .letterhead__name {
    position: absolute; left: 98px; top: 30px;
    font-family: "Comfortaa", sans-serif; font-size: 40px; font-weight: 400;
    color: var(--white); letter-spacing: 1px;
  }
  .letterhead__label {
    position: absolute; right: 40px; top: 84px;
    font-size: 15px; font-weight: 700; color: var(--ink);
  }
  .letterhead__footer {
    position: absolute; left: 0; bottom: 0; width: 100%; height: 110px;
    padding: 22px 28px; display: flex; justify-content: space-between;
    font-size: 12px; font-weight: 500; color: var(--ink-soft); line-height: 1.5;
  }
  .footer-web span { display: inline-block; width: 62px; }
  .footer-web .indent { padding-left: 62px; }
  .footer-contact { align-self: flex-end; }
  .footer-contact svg { vertical-align: -3px; margin-right: 4px; }

  /* Business cards */
  .card {
    position: absolute; width: 440px; height: 252px;
    background: var(--card); box-shadow: 0 4px 14px rgba(0,0,0,0.2);
    overflow: hidden; color: var(--ink);
  }
  .card--dunmore { left: 740px; top: 150px; }
  .card--haskell { left: 740px; top: 560px; }
  .card .brand-dot { left: 200px; top: 18px; width: 40px; height: 40px; }
  .card__name {
    position: absolute; left: 0; top: 70px; width: 100%; text-align: center;
    font-family: "Comfortaa", sans-serif; font-size: 27px; color: var(--white);
  }
  .card__person { position: absolute; right: 44px; top: 126px; text-align: center; }
  .card__person-name { font-weight: 700; font-size: 15px; text-decoration: underline; color: var(--ink); }
  .card__person-role { font-size: 12px; color: var(--white); }
  .card__details {
    position: absolute; left: 28px; top: 138px; font-size: 12.5px; font-weight: 500; line-height: 1.85;
  }
  .card__details svg { vertical-align: -4px; margin-right: 6px; }
</style>
</head>
<body>

  <section class="letterhead">
    <div class="letterhead__header">
      <span class="brand-dot"></span>
      <h1 class="letterhead__name">Haskell and Dunmore</h1>
      <p class="letterhead__label">LetterHead</p>
    </div>
    <div class="letterhead__stripe letterhead__stripe--top"></div>
    <div class="letterhead__stripe letterhead__stripe--bottom"></div>
    <footer class="letterhead__footer">
      <div class="footer-web">
        <p><span>Website:</span>www.haskellanddunmore.com</p>
        <p><span>Email:</span>haskellw@ranchmail.com&nbsp; or</p>
        <p class="indent">jo@haskellanddunmore.com</p>
      </div>
      <div class="footer-contact">
        <p># 408 W Oak St. Junction, TX 76849</p>
        <p><svg width="10" height="16" viewBox="0 0 10 16"><rect x="0.5" y="0.5" width="9" height="15" rx="2" fill="#1d2a4a"/><rect x="2" y="2.5" width="6" height="8" fill="#8aa"/></svg>512-555-0187 or 325-555-0146</p>
      </div>
    </footer>
  </section>

  <article class="card card--dunmore">
    <span class="brand-dot"></span>
    <h2 class="card__name">Haskell and Dunmore</h2>
    <div class="card__person">
      <p class="card__person-name">T. Jo Dunmore</p>
      <p class="card__person-role">Agent</p>
    </div>
    <div class="card__details">
      <p><svg width="10" height="16" viewBox="0 0 10 16"><rect x="0.5" y="0.5" width="9" height="15" rx="2" fill="#1d2a4a"/><rect x="2" y="2.5" width="6" height="8" fill="#8aa"/></svg>325-555-0146</p>
      <p>Email:&nbsp; jo@haskellanddunmore.com</p>
      <p>Website:&nbsp; www.haskellanddunmore.com</p>
      <p># 408 W Oak St. Junction, TX 76849</p>
    </div>
  </article>

  <article class="card card--haskell">
    <span class="brand-dot"></span>
    <h2 class="card__name">Haskell and Dunmore</h2>
    <div class="card__person">
      <p class="card__person-name">Wade Haskell</p>
      <p class="card__person-role">Agent</p>
    </div>
    <div class="card__details">
      <p><svg width="10" height="16" viewBox="0 0 10 16"><rect x="0.5" y="0.5" width="9" height="15" rx="2" fill="#1d2a4a"/><rect x="2" y="2.5" width="6" height="8" fill="#8aa"/></svg>512-555-0187</p>
      <p>Email:&nbsp; haskellw@ranchmail.com</p>
      <p>Website:&nbsp; www.haskellanddunmore.com</p>
      <p># 408 W Oak St. Junction, TX 76849</p>
    </div>
  </article>

</body>
</html>
```